Flyer
Der Flyer ist super geworden. Vielen Dank! :-)
Zielgruppe
Wir sind Hersteller von Unterkonstruktion für PV-Anlagen. Unsere Zielgruppe sind Monteure oder Firmen die PV-Anlagen verbauen.
Aufgabenstellung
Ich hätte gerne einen Slogan wie Bestpreisgarantie. Oder: Unterkonstruktionen in bester Qualität – zum besten Preis
Oder Sie haben selbst Vorschläge; Wenn möglich können Sie gerne die Bilder von der pptx Datei nehmen. Wir haben auf den Clip unter der Hammerkopfschraube ein Patent (liegt bei), dieser Clip ist ein deutlicher Vorteil bei der Verbauung, damit sich die Hammerkopfschraube beim Verbauen nicht verdreht.
Unsere Adresse sollte noch auf den Flyer:
KD Lumatrix Werke GmbH, Falkenhainweg 14, 80417 München
Fon: 089 518 327 40 Mail: info@kdlumatrixwerke.com
Website: www.kdlumatrixwerke.com

```html
<!DOCTYPE html>
<html lang="de">
<head>
<meta charset="utf-8">
<title>KD Lumatrix Werke – Flyer</title>
<link rel="stylesheet" href="https://fonts.googleapis.com/css2?family=Montserrat:wght@800;900&family=Mulish:wght@300;400;600;700;800&display=swap">
<style>
:root{
  --bg:#ebebeb;
  --navy:#283583;
  --sky:#7b96c9;
  --pale:#d9e0ec;
  --white:#ffffff;
  --head:"Montserrat",sans-serif;
  --body:"Mulish",sans-serif;
}
*{margin:0;padding:0;box-sizing:border-box}
html,body{width:768px;height:1200px;overflow:hidden;background:var(--bg)}
.sheet{position:relative;width:768px;height:1200px;font-family:var(--body);color:var(--navy)}
.label{position:absolute;font-family:var(--body);font-weight:800;font-size:24px;color:var(--navy);line-height:1}
.label--front{left:286px;top:48px}
.label--inside{left:144px;top:386px}
.label--back{left:423px;top:1112px}
.page{position:absolute;overflow:hidden;box-shadow:0 4px 9px rgba(0,0,0,.28)}
.page svg.overlay{position:absolute;left:0;top:0}
.photo{position:absolute}
.front{left:385px;top:51px;width:240px;height:340px}
.front .photo{inset:0;background:linear-gradient(125deg,#5f6270 0%,#8b8d97 30%,#b0643f 38%,#6b6e7a 44%,#9a9ca6 62%,#5b5e6b 80%,#a4663f 100%)}
.brand{position:absolute;left:36.5px;top:0;width:170px;height:110.5px;background:var(--white);text-align:center}
.brand__name{position:absolute;left:0;right:0;top:52px;font-family:var(--body);font-weight:600;font-size:14px;letter-spacing:.3px;color:var(--navy)}
.brand__tag{position:absolute;left:0;right:0;top:77px;font-weight:300;font-size:8.8px;line-height:11.5px;color:var(--navy)}
.inside{left:144.5px;top:421px;width:481px;height:340.5px}
.cell{position:absolute;width:120.25px;height:170.25px;text-align:center}
.cell--pale{background:var(--pale);color:var(--navy)}
.cell--navy{background:var(--navy);color:var(--white)}
.cell--white{background:var(--white)}
.cell__icon{display:block;margin:16px auto 0}
.cell__title{font-weight:800;font-size:7.3px;line-height:9.5px;margin-top:9px}
.cell__text{font-weight:400;font-size:5.5px;line-height:8.6px;margin:2px auto 0;width:100px}
.tag{position:absolute;background:var(--white);color:var(--navy);font-size:4.6px;font-weight:600;padding:1px 2px;line-height:6px;white-space:nowrap}
.back{left:144.5px;top:790.5px;width:241px;height:340.5px}
.back .photo{inset:0;background:linear-gradient(120deg,#9c9ea6 0%,#b5b7bd 28%,#b4653d 36%,#5c5f6c 46%,#5a5d6a 60%,#a25f3a 72%,#4f5260 84%,#9fb8b8 100%)}
.cta{position:absolute;left:25.5px;top:163px;font-family:var(--head);font-weight:900;font-size:13.6px;line-height:15px;color:var(--navy)}
.contact{position:absolute;left:25.5px;top:226px;font-weight:800;font-size:8.3px;line-height:10.3px;color:var(--white)}
.address{position:absolute;left:21px;top:261px;font-size:5.5px;line-height:8.6px;color:var(--white);font-weight:400}
.address strong{font-weight:800}
</style>
</head>
<body>
<main class="sheet">

  <div class="label label--front">Vorne</div>
  <section class="page front">
    <div class="photo" role="img" aria-label="Foto: Solarmodule auf einem Ziegeldach"></div>
    <div class="brand">
      <div class="brand__name">KD LUMATRIX WERKE</div>
      <div class="brand__tag">Unterkonstruktionen für<br>eine standhafte Zukunft!</div>
    </div>
    <svg class="overlay" width="240" height="340" viewBox="0 0 240 340">
      <polygon points="120,157.5 240,157.5 240,228 74,228" fill="var(--sky)"/>
      <polygon points="122.5,228 240,228 240,278 95,278" fill="var(--navy)"/>
      <text x="120" y="189" font-family="Montserrat,sans-serif" font-weight="900" font-size="19" fill="#fff">BESTPREIS-</text>
      <text x="120" y="211" font-family="Montserrat,sans-serif" font-weight="900" font-size="19" fill="#fff">GARANTIE</text>
      <g font-family="Mulish,sans-serif" font-weight="600" font-size="9" fill="#fff">
        <text x="133" y="245">Unterkonstruktionen</text>
        <text x="133" y="256.5">in bester Qualität –</text>
        <text x="133" y="268">zum besten Preis</text>
      </g>
    </svg>
  </section>

  <div class="label label--inside">Innen</div>
  <section class="page inside">
    <div class="cell cell--pale" style="left:0;top:0">
      <svg class="cell__icon" width="38" height="38" viewBox="0 0 38 38"><circle cx="19" cy="19" r="17" fill="none" stroke="var(--navy)" stroke-width="2.4"/><path d="M19 11v16M11 19h16" stroke="var(--navy)" stroke-width="2.6"/></svg>
      <div class="cell__title">Zuverlässige<br>Konstruktionen</div>
      <p class="cell__text">Die 100%ige Liefertreue und Qualität wird durch die langjährige Produktionserfahrung und ständige Überwachung der Lieferanten sichergestellt.</p>
    </div>
    <div class="photo" style="left:120.25px;top:0;width:120.25px;height:170.25px;background:linear-gradient(140deg,#8a93b5 0%,#5f6a96 45%,#2b2f45 65%,#3f58b5 100%)" role="img" aria-label="Foto: Monteur mit Laptop auf Solarmodulen"></div>
    <div class="cell cell--navy" style="left:240.5px;top:0">
      <svg class="cell__icon" width="38" height="38" viewBox="0 0 38 38"><path d="M19 2 A17 17 0 1 0 36 19" fill="none" stroke="#fff" stroke-width="2.4"/><circle cx="26" cy="4" r="1.3" fill="#fff"/><circle cx="31" cy="7.5" r="1.3" fill="#fff"/><circle cx="34.3" cy="12.5" r="1.3" fill="#fff"/></svg>
      <div class="cell__title">Reduzierte Montagezeit</div>
      <p class="cell__text">Profilschienen und patentierte Verbindungselemente garantieren hohe Sicherheit, Flexibilität und universellen Einsatz.</p>
    </div>
    <div class="photo" style="left:360.75px;top:0;width:120.25px;height:170.25px;background:linear-gradient(160deg,#f4f4f4 0%,#7a7a7e 35%,#c8a878 65%,#a88a5e 100%)" role="img" aria-label="Technische Zeichnung: Profilschiene mit Hammerkopf, Kunststoff-Clip und Winkel">
      <span class="tag" style="left:57px;top:43px">← Profilschiene</span>
      <span class="tag" style="left:60.5px;top:105px">← Hammerkopf</span>
      <span class="tag" style="left:71.5px;top:126px">← Kunststoff Clip</span>
      <span class="tag" style="left:52px;top:149px">← Winkel</span>
    </div>

    <div class="photo" style="left:0;top:170.25px;width:120.25px;height:170.25px;background:linear-gradient(170deg,#d8d8d8 0%,#9fa3b0 30%,#c9b7a6 55%,#6f86c6 100%)" role="img" aria-label="Foto: Hand montiert Solarmodul mit Werkzeug"></div>
    <div class="cell cell--navy" style="left:120.25px;top:170.25px">
      <svg class="cell__icon" width="38" height="38" viewBox="0 0 38 38"><circle cx="19" cy="19" r="17" fill="none" stroke="#fff" stroke-width="2.4"/><path d="M13 25L25 13M16 13h9v9" fill="none" stroke="#fff" stroke-width="2.6"/></svg>
      <div class="cell__title">Preisvorteil</div>
      <p class="cell__text">Sehr günstige Einkaufspreise und hervorragende Qualität bei den Unterkonstruktionssystemen durch langjährige Erfahrung mit Herstellern und Lieferanten aus dem DACH-Gebiet.</p>
    </div>
    <div class="cell cell--white" style="left:240.5px;top:170.25px">
      <svg width="120" height="170" viewBox="0 0 120 170">
        <rect x="10" y="32" width="42" height="14" rx="2" fill="#c9d1e6"/>
        <circle cx="82" cy="39" r="12" fill="#3f6fb3"/>
        <rect x="13" y="76" width="28" height="22" rx="2" fill="#c9d1e6"/>
        <rect x="72" y="80" width="20" height="14" rx="2" fill="#d6d6d6"/>
        <rect x="17" y="120" width="20" height="28" rx="2" fill="#d6d6d6"/>
        <circle cx="82" cy="134" r="13" fill="#e6b12a"/>
      </svg>
    </div>
    <div class="cell cell--pale" style="left:360.75px;top:170.25px">
      <svg class="cell__icon" width="38" height="38" viewBox="0 0 38 38"><circle cx="19" cy="19" r="17" fill="none" stroke="var(--navy)" stroke-width="2.4"/><path d="M11 18l6 8 11-15" fill="none" stroke="var(--navy)" stroke-width="2.6"/></svg>
      <div class="cell__title">Sicherheit</div>
      <p class="cell__text">Unser Unternehmen, die Produktion und Materialien sind auditiert und zertifiziert.</p>
    </div>
    <svg class="overlay" width="481" height="341" viewBox="0 0 481 341">
      <polygon points="120,62 137,79 120,96" fill="var(--pale)"/>
      <polygon points="360.5,62 378,79 360.5,96" fill="var(--navy)"/>
      <polygon points="120.5,232 103,249 120.5,266" fill="var(--navy)"/>
      <polygon points="361,232 343.5,249 361,266" fill="var(--pale)"/>
    </svg>
  </section>

  <section class="page back">
    <div class="photo" role="img" aria-label="Foto: Solarthermie- und Photovoltaikmodule mit Dachfenster"></div>
    <svg class="overlay" width="241" height="341" viewBox="0 0 241 341">
      <polygon points="115.5,198.5 128,198.5 164.5,258 0,258 0,216" fill="var(--navy)"/>
      <polygon points="0,157 88,157 123,216 0,216" fill="var(--white)"/>
      <polygon points="0,258 108,258 133,294.5 0,294.5" fill="var(--sky)"/>
    </svg>
    <div class="cta">JETZT<br>BERATEN<br>LASSEN!</div>
    <div class="contact">089 518 327 40<br>info@kdlumatrixwerke.com</div>
    <div class="address"><strong>KD Lumatrix Werke GmbH,</strong><br>Falkenhainweg 14, 80417 München<br>www.kdlumatrixwerke.com</div>
  </section>
  <div class="label label--back">Rückseite</div>

</main>
</body>
</html>
```